Mobile welding fabrication and repair, heavy equipment and semi repair

We need a business card design that will catch the eye but look prelesional at the same time. Were based out of Idaho and we do all welding fabrication jobs and repairs, we also build and install custom pipe fences for personal or larger scale fence jobs and can give free quotes. We can do semi truck and trailer repairs Mobily also.

Target Market(s)

Welding

Industry/Entity Type

welding and repair

Contact Information for Business Card

email (flintforgeandfix@mailvero.com, phone number 208-417-3862, owner (Wade Pellston), Pipe Fence, Semi Repair, Mobile welding and fabrication

Font styles to use
Sans Serif

Requirements
Must have
• My logo in black background on one side , and other side my logo in white back round with all the information listed on card details
Nice to have
• make it stand out from other business cards

```html
<!DOCTYPE html>
<html lang="en">
<head>
<meta charset="utf-8">
<title>Flint Forge and Fix — Business Card</title>
<link rel="stylesheet" href="https://fonts.googleapis.com/css2?family=Michroma&family=Oswald:wght@600&family=Quicksand:wght@500&display=swap">
<style>
  :root {
    --page-bg: #2b2c2e;
    --card-black: #050506;
    --brand-blue: #1f8fe0;
    --swoosh-blue: #1f5fb8;
    --band-blue-a: #1c3fae;
    --band-blue-b: #2a5fd0;
    --plate-navy-a: #0a1236;
    --plate-navy-b: #1b3266;
    --silver: #c9ced6;
    --white: #ffffff;
    --icon-blue: #1aa3f0;
  }
  * { box-sizing: border-box; margin: 0; padding: 0; }
  html, body { width: 1200px; height: 900px; overflow: hidden; }
  body {
    background: var(--page-bg);
    display: flex;
    flex-direction: column;
    align-items: center;
    justify-content: center;
    gap: 48px;
  }
  .card {
    position: relative;
    width: 640px;
    height: 366px;
    border-radius: 22px;
    overflow: hidden;
    background: var(--card-black);
    box-shadow: 0 10px 30px rgba(0,0,0,.45);
  }
  .wordmark {
    font-family: "Michroma", sans-serif;
    color: var(--brand-blue);
    font-size: 30px;
    letter-spacing: 2px;
    line-height: 1.25;
    white-space: nowrap;
  }
  /* front */
  .card-front .swoosh { position: absolute; inset: 0; }
  .card-front .wordmark {
    position: absolute;
    left: 130px;
    top: 140px;
    text-align: center;
  }
  /* back */
  .card-back .header {
    position: absolute;
    left: 0; top: 0;
    width: 100%; height: 132px;
    background: var(--card-black);
  }
  .card-back .wordmark {
    position: absolute;
    left: 30px; top: 84px;
    font-size: 24px;
  }
  .owner {
    position: absolute;
    right: 32px; top: 24px;
    text-align: right;
    font-family: "Michroma", sans-serif;
    white-space: nowrap;
  }
  .owner-name { color: var(--brand-blue); font-size: 18px; letter-spacing: 1px; }
  .owner-role { color: var(--white); font-size: 13px; letter-spacing: 1px; margin-top: 2px; }
  .rule {
    position: absolute; left: 0; width: 100%; height: 4px;
    background: linear-gradient(90deg, #6d737c, var(--silver), #ffffff, var(--silver), #6d737c);
  }
  .rule-top { top: 132px; }
  .rule-bottom { top: 292px; }
  .plate {
    position: absolute;
    left: 0; top: 136px;
    width: 100%; height: 156px;
    background: radial-gradient(ellipse at 55% 30%, var(--plate-navy-b), var(--plate-navy-a) 75%);
  }
  .contact {
    position: absolute;
    left: 34px; top: 186px;
    display: grid;
    grid-template-columns: 30px auto;
    column-gap: 12px;
    row-gap: 8px;
    align-items: center;
    white-space: nowrap;
  }
  .contact-icon {
    width: 30px; height: 30px;
    border-radius: 50%;
    background: var(--icon-blue);
    display: flex; align-items: center; justify-content: center;
  }
  .contact-phone {
    font-family: "Michroma", sans-serif;
    font-size: 24px;
    color: var(--white);
    letter-spacing: 1px;
  }
  .contact-email {
    font-family: "Quicksand", sans-serif;
    font-size: 19px;
    color: var(--white);
  }
  .services {
    position: absolute;
    left: 0; top: 296px;
    width: 100%; height: 70px;
    padding: 0 24px;
    background: linear-gradient(90deg, var(--band-blue-a), var(--band-blue-b));
    display: flex; align-items: center; justify-content: center;
    gap: 12px;
    font-family: "Oswald", sans-serif;
    font-weight: 600;
    font-size: 20px;
    line-height: 1;
    color: var(--white);
    letter-spacing: .3px;
    text-transform: uppercase;
    white-space: nowrap;
  }
  .services span { flex: none; }
  .services .dot { width: 6px; height: 6px; border-radius: 50%; background: var(--white); }
</style>
</head>
<body>

  <section class="card card-front" aria-label="Card front">
    <svg class="swoosh" width="640" height="366" viewBox="0 0 640 366" aria-hidden="true">
      <path d="M470 0 C560 60 600 200 520 366 L640 366 L640 0 Z" fill="var(--swoosh-blue)"/>
      <path d="M440 0 C530 70 560 210 470 366 L520 366 C600 200 560 60 470 0 Z" fill="var(--card-black)"/>
    </svg>
    <div class="wordmark">FLINT FORGE<br>AND FIX</div>
  </section>

  <section class="card card-back" aria-label="Card back">
    <div class="header">
      <div class="wordmark">FLINT FORGE AND FIX</div>
      <div class="owner">
        <div class="owner-name">WADE PELLSTON</div>
        <div class="owner-role">OWNER</div>
      </div>
    </div>
    <div class="rule rule-top"></div>
    <div class="plate" role="img" aria-label="Dark blue diamond-plate steel texture"></div>
    <div class="contact">
      <span class="contact-icon">
        <svg width="16" height="16" viewBox="0 0 24 24" aria-hidden="true"><path fill="#fff" d="M6.6 10.8a15.1 15.1 0 0 0 6.6 6.6l2.2-2.2c.3-.3.7-.4 1-.2 1.1.4 2.3.6 3.6.6.6 0 1 .4 1 1V20c0 .6-.4 1-1 1C10.6 21 3 13.4 3 4c0-.6.4-1 1-1h3.5c.6 0 1 .4 1 1 0 1.3.2 2.5.6 3.6.1.3 0 .7-.2 1z"/></svg>
      </span>
      <span class="contact-phone">208-417-3862</span>
      <span class="contact-icon">
        <svg width="16" height="16" viewBox="0 0 24 24" aria-hidden="true"><rect x="3" y="6" width="18" height="12" rx="1.5" fill="#fff"/><path d="M3.5 6.5 12 13l8.5-6.5" stroke="var(--icon-blue)" stroke-width="1.6" fill="none"/></svg>
      </span>
      <span class="contact-email">flintforgeandfix@mailvero.com</span>
    </div>
    <div class="rule rule-bottom"></div>
    <div class="services">
      <span>Pipe Fence</span><span class="dot"></span>
      <span>Semi Repair</span><span class="dot"></span>
      <span>Mobile Welding and Fabrication</span>
    </div>
  </section>

</body>
</html>
```